Mine Engineering Consultancy specializing in
* Pit optimization
* Mine Design
* Scheduling
* Mine Rehabilitation

Industry/Entity Type

Mining

Contact Information for Business Card

RVT Mining Pty Ltd
Derek Holloway
Director/Principle Mining Engineer
Mobile 0413582961
Email derek.holloway@rvtmining-example.com

```html
<!DOCTYPE html>
<html lang="en">
<head>
<meta charset="utf-8">
<title>RVT Mining Pty Ltd – Business Card</title>
<link rel="stylesheet" href="https://fonts.googleapis.com/css2?family=Crimson+Text:wght@400;600&display=swap">
<style>
  :root {
    --stage: #e6e4e0;
    --card-white: #f7f7f7;
    --ink: #2b2b2b;
    --ink-soft: #444444;
    --brand-blue: #3a7cc0;
    --band-blue: #1f6fb8;
    --night: #050507;
    --services-blue: #3c3f9c;
    --plan-line: #14183a;
    --list-white: #e9e9e9;
  }
  * { margin: 0; padding: 0; box-sizing: border-box; }
  html, body {
    width: 1200px; height: 902px; overflow: hidden;
    background: var(--stage);
    font-family: "Crimson Text", Georgia, serif;
  }
  .canvas {
    width: 1200px; height: 902px;
    display: flex; flex-direction: column; align-items: center; justify-content: center;
    gap: 40px;
  }
  .card {
    position: relative; width: 700px; height: 400px; overflow: hidden;
    box-shadow: 0 6px 18px rgba(0,0,0,.18);
  }

  /* Back: services */
  .card-back { background: var(--night); color: var(--list-white); text-align: center; }
  .pit-plan {
    position: absolute; inset: 40px 20px 30px 20px;
    background: radial-gradient(ellipse at 50% 45%, var(--plan-line) 0%, rgba(20,24,58,.35) 45%, transparent 75%);
  }
  .services-title {
    position: relative; padding-top: 62px;
    font-size: 52px; font-weight: 400; color: var(--services-blue); line-height: 1;
  }
  .services-list { position: relative; list-style: none; margin-top: 26px; font-size: 28px; line-height: 1.45; }

  /* Front: contact */
  .card-front { background: var(--card-white); }
  .company-name {
    position: absolute; left: 44px; top: 205px;
    font-size: 27px; font-weight: 400; color: var(--brand-blue);
  }
  .divider { position: absolute; left: 330px; top: 55px; width: 2px; height: 240px; background: var(--ink-soft); }
  .contact { position: absolute; left: 362px; top: 52px; color: var(--ink); }
  .person-name { font-size: 33px; font-weight: 600; line-height: 1.1; }
  .person-role { font-size: 21px; color: var(--ink-soft); margin-top: 2px; }
  .contact-lines { list-style: none; margin-top: 34px; font-size: 21px; line-height: 1.75; }
  .contact-lines li { display: flex; align-items: center; gap: 10px; }
  .contact-icon { width: 17px; height: 17px; flex: none; }
  .front-bands { position: absolute; left: 0; bottom: 0; width: 700px; height: 400px; pointer-events: none; }
</style>
</head>
<body>
<main class="canvas">

  <section class="card card-back" aria-label="Card back">
    <div class="pit-plan" role="img" aria-label="Faint blue line plan of an open pit mine"></div>
    <h2 class="services-title">Services</h2>
    <ul class="services-list">
      <li>Pit optimization</li>
      <li>Mine Design</li>
      <li>Scheduling</li>
      <li>Mine Rehabilitation</li>
    </ul>
  </section>

  <section class="card card-front" aria-label="Card front">
    <svg class="front-bands" viewBox="0 0 700 400" aria-hidden="true">
      <path d="M0 338 H372 Q388 338 392 320 L397 300 Q401 286 416 286 L700 262 V400 H0Z" fill="var(--band-blue)"/>
      <path d="M408 400 L414 318 Q416 302 432 302 L700 278 V400Z" fill="var(--night)"/>
      <path d="M402 400 L408 318 Q410 298 430 298 L700 274" fill="none" stroke="var(--card-white)" stroke-width="3"/>
    </svg>

    <p class="company-name">RVT Mining Pty Ltd</p>
    <div class="divider"></div>

    <div class="contact">
      <h1 class="person-name">Derek Holloway</h1>
      <p class="person-role">Director/Principle Mining Engineer</p>
      <ul class="contact-lines">
        <li>
          <svg class="contact-icon" viewBox="0 0 16 16" aria-hidden="true"><rect width="16" height="16" rx="2" fill="var(--ink)"/><path d="M5 3.5 L6.6 6 L5.6 7 Q6.6 9.4 9 10.4 L10 9.4 L12.5 11 L11.5 12.6 Q6 12 3.4 4.5Z" fill="var(--card-white)"/></svg>
          <span>0413582961</span>
        </li>
        <li>
          <svg class="contact-icon" viewBox="0 0 16 16" aria-hidden="true"><rect width="16" height="16" rx="2" fill="var(--ink)"/><rect x="3" y="4.5" width="10" height="7" fill="none" stroke="var(--card-white)" stroke-width="1.2"/><path d="M3 4.5 L8 8.5 L13 4.5" fill="none" stroke="var(--card-white)" stroke-width="1.2"/></svg>
          <span>derek.holloway@rvtmining-example.com</span>
        </li>
      </ul>
    </div>
  </section>

</main>
</body>
</html>
```